Web page for analytics company

Now that I have a new logo, I need a webpage design that will use it to its potential. Am looking for a design that handles presentation and access to data well - like sites with blocks that provide direct access to content without going through a set of menus. More like an infographic. No left/right menu bar.

I want the logo (attached) against a black background, but not text - not a fan of trying to read white text on a dark screen.

The website - morvilent.com - currently has four pages - home, who we are, by the numbers and a blog.

The site will be done in Squarespace.

My apologies for not responding promptly - big report due today.  I will be online tomorrow with answers and feedback. 

Thanks!

```html
<!DOCTYPE html>
<html lang="en">
<head>
<meta charset="utf-8">
<title>Morvilent – Parity Insight Metrics</title>
<link rel="stylesheet" href="https://fonts.googleapis.com/css2?family=Arimo:ital,wght@0,400;0,700;1,400;1,700&family=Open+Sans:ital,wght@0,400;0,600;1,400;1,600&display=swap">
<style>
  :root {
    --page-bg: #ffffff;
    --ink-dark: #231f20;
    --content-bg: #ece8e7;
    --tile-bg: #bdb3b3;
    --tile-ink: #2e2a2b;
    --body-ink: #3a3536;
    --rule: #8e8788;
    --white: #ffffff;
    --accent: #f0931e;
    --sky-top: #5d7590;
    --sky-mid: #9aa9b9;
    --sky-low: #c9cfd4;
    --field: #7a7a62;
    --input-top: #ffffff;
    --input-bottom: #b9b9b9;
    --social-a: #2d4f8c;
    --social-b: #2fa6dc;
    --social-c: #d2392d;
  }
  * { box-sizing: border-box; margin: 0; padding: 0; }
  html, body { width: 1200px; height: 1000px; overflow: hidden; background: var(--page-bg); }
  body { position: relative; font-family: "Open Sans", Tahoma, sans-serif; }

  .page { position: absolute; left: 171px; top: 0; width: 918px; height: 1000px; background: var(--content-bg); }

  .site-header { position: absolute; left: 0; top: 0; width: 918px; height: 100px; background: var(--ink-dark); }
  .brand { position: absolute; display: flex; align-items: center; gap: 8px; color: var(--white);
           font-family: "Arimo", Arial, sans-serif; font-weight: 400; }
  .brand-dot { width: 30px; height: 30px; border-radius: 50%; background: var(--accent); }
  .site-header .brand { left: 172px; top: 30px; font-size: 29px; }

  .hero { position: absolute; left: 0; top: 100px; width: 918px; height: 304px; }
  .hero-photo { position: absolute; inset: 0;
    background:
      radial-gradient(ellipse 120px 160px at 570px 190px, rgba(225,225,225,.8), rgba(225,225,225,0) 70%),
      linear-gradient(180deg, var(--sky-top) 0%, var(--sky-mid) 45%, var(--sky-low) 80%, var(--field) 100%); }
  .hero-title { position: absolute; left: 171px; top: 38px; color: var(--white);
    font-family: "Arimo", Arial, sans-serif; font-style: italic; font-weight: 700; font-size: 28px; letter-spacing: 2.4px; white-space: nowrap; }
  .hero-tagline { position: absolute; left: 172px; top: 84px; color: var(--white);
    font-family: "Arimo", Arial, sans-serif; font-style: italic; font-weight: 700; font-size: 11px; letter-spacing: 1.3px; white-space: nowrap; }
  .hero-quote { position: absolute; left: 168px; top: 186px; color: var(--white); font-style: italic; white-space: nowrap; }
  .hero-quote .lead { font-size: 11px; line-height: 14px; }
  .hero-quote .emph { font-weight: 600; font-size: 13.6px; line-height: 17px; margin-top: 4px; }
  .hero-quote cite { display: block; font-size: 9px; margin: 8px 0 0 16px; }

  .section-nav { position: absolute; left: 200px; top: 408px; display: flex; gap: 3px; }
  .nav-tile { width: 127px; height: 109px; background: var(--tile-bg); color: var(--tile-ink);
    text-decoration: none; display: flex; flex-direction: column; align-items: center; justify-content: flex-end;
    padding-bottom: 15px; font-size: 13.5px; }
  .nav-tile svg { margin-bottom: 4px; fill: var(--tile-ink); }
  .nav-rule { position: absolute; left: 54px; top: 519px; width: 811px; height: 2px; }

  .intro { position: absolute; left: 165px; top: 552px; width: 620px; color: var(--body-ink);
    font-size: 10.6px; line-height: 13.4px; white-space: nowrap; }
  .intro p { margin-bottom: 13.4px; }

  .site-footer { position: absolute; left: 0; top: 823px; width: 918px; height: 177px; background: var(--ink-dark); color: var(--white); }
  .site-footer .brand { left: 38px; top: 24px; font-size: 28px; }
  .footer-links { position: absolute; left: 93px; top: 68px; list-style: none;
    font-family: "Arimo", Arial, sans-serif; font-weight: 700; font-size: 11px; line-height: 19.5px; letter-spacing: .5px; }
  .footer-links a { color: var(--white); text-decoration: none; }
  .signup { position: absolute; left: 367px; top: 17px; width: 220px; font-family: "Arimo", Arial, sans-serif; }
  .signup h3 { font-size: 11.5px; letter-spacing: .8px; margin-bottom: 4px; }
  .signup label { display: block; font-size: 8px; font-weight: 700; margin-top: 5px; }
  .signup label:first-of-type { margin-top: 0; }
  .signup input { display: block; width: 217px; height: 25px; border: 1px solid #555;
    background: linear-gradient(180deg, var(--input-top), var(--input-bottom)); margin-top: 1px; }
  .follow { position: absolute; left: 753px; top: 32px; font-family: "Arimo", Arial, sans-serif; }
  .follow h3 { font-size: 11px; letter-spacing: .6px; margin-bottom: 8px; }
  .social { display: flex; gap: 12px; }
  .social span { width: 28px; height: 28px; display: block; }
  .copyright { position: absolute; right: 14px; bottom: 7px; font-family: "Arimo", Arial, sans-serif; font-size: 9px; }
</style>
</head>
<body>
<div class="page">
  <header class="site-header">
    <div class="brand"><span class="brand-dot"></span>Morvilent</div>
  </header>

  <section class="hero">
    <div class="hero-photo" role="img" aria-label="Photo of a woman with arms raised in a field beneath a cloudy blue sky"></div>
    <h1 class="hero-title">PARITY INSIGHT METRICS</h1>
    <p class="hero-tagline">IMPROVING RESULTS BY MEASURING WHAT MATTERS</p>
    <blockquote class="hero-quote">
      <p class="lead">"We keep statistics on everything we care about, from RBIs to ROI,<br>the daily ups and downs of the Dow and our bank accounts...</p>
      <p class="emph">So if we’re serious about narrowing the gender gap and<br>helping more girls and women, then we must get serious<br>&nbsp;about gathering and analyzing the data that tell the tale."</p>
      <cite>- Former public servant Eleanor Whitcombe, July 2012</cite>
    </blockquote>
  </section>

  <nav class="section-nav">
    <a class="nav-tile" href="#">
      <svg width="56" height="58" viewBox="0 0 56 58"><path d="M28 2 L54 28 H47 V56 H33 V40 H23 V56 H9 V28 H2 Z"/></svg>Home</a>
    <a class="nav-tile" href="#">
      <svg width="56" height="58" viewBox="0 0 56 58"><rect x="2" y="34" width="14" height="24" rx="2"/><rect x="21" y="16" width="14" height="42" rx="2"/><rect x="40" y="0" width="14" height="58" rx="2"/></svg>By The Numbers</a>
    <a class="nav-tile" href="#">
      <svg width="60" height="50" viewBox="0 0 60 50"><circle cx="38" cy="12" r="11"/><path d="M20 44 C20 30 28 24 38 24 C48 24 58 30 58 44 Z"/><circle cx="22" cy="16" r="12" stroke="var(--tile-bg)" stroke-width="2"/><path d="M0 50 C0 36 10 29 22 29 C34 29 44 36 44 50 Z" stroke="var(--tile-bg)" stroke-width="2"/></svg>Who We Are</a>
    <a class="nav-tile" href="#">
      <svg width="48" height="58" viewBox="0 0 48 58"><path d="M0 0 H34 L48 14 V58 H0 Z"/><path d="M34 0 V14 H48" fill="var(--tile-bg)"/><g fill="var(--tile-bg)"><rect x="8" y="20" width="32" height="3"/><rect x="8" y="28" width="32" height="3"/><rect x="8" y="36" width="32" height="3"/><rect x="8" y="44" width="32" height="3"/></g></svg>Blog</a>
  </nav>
  <svg class="nav-rule" viewBox="0 0 811 2" style="overflow:visible">
    <path d="M0 1 H200 L208 -7 L216 1 H811" fill="var(--content-bg)" stroke="var(--rule)" stroke-width="1"/>
  </svg>

  <main class="intro">
    <p>As much as we'd like to think that treating everyone equally is the best strategy for fairness, the reality is that the<br>differences in the lives of women and men have to be taken into account to ensure that organizations, programs,<br>services, and yes, even public policy treat women and men in ways that achieve gender equity.</p>
    <p>That's where Morvilent - Parity Insight Metrics - comes in.&nbsp; Using the data-driven tools of gender analysis,<br>we can help you determine if gender equity is being achieved - in businesses and organizations, in the planning<br>and implementation of programs and services, and in the development and enforcement of public policy.</p>
    <p>The evidence is in: analysis of organizational performance metrics that date back to the 1980s shows there is<br>a clear relationship between better results and diverse leadership. Senior executives who ignore the data do so to<br>their detriment. They're literally leaving money on the table.</p>
    <p>But numbers don't tell the whole story.&nbsp; Organizations have to be willing to dig deep to discover where the biases<br>are buried - in the organization's culture, in governance practices, in talent management strategies, and in personal<br>values and belief systems.</p>
    <p>Find out what a gender equity audit can do for your organization.<br>Contact us at hbrandt@morvilent.com or 555-018-4472.</p>
  </main>

  <footer class="site-footer">
    <div class="brand"><span class="brand-dot"></span>Morvilent</div>
    <ul class="footer-links">
      <li><a href="#">Home</a></li>
      <li><a href="#">By The Numbers</a></li>
      <li><a href="#">Who We Are</a></li>
      <li><a href="#">Blog</a></li>
    </ul>
    <form class="signup">
      <h3>Subscribe to our mailing list</h3>
      <label>Email:<input type="email"></label>
      <label>First Name:<input type="text"></label>
      <label>Last Name:<input type="text"></label>
    </form>
    <div class="follow">
      <h3>Follow Us:</h3>
      <div class="social">
        <span style="background:var(--social-a)"></span>
        <span style="background:var(--social-b)"></span>
        <span style="background:var(--social-c)"></span>
      </div>
    </div>
    <p class="copyright">Copyright © 2014 Morvilent. All rights reserved.</p>
  </footer>
</div>
</body>
</html>
```